High Design Value Gift Webstore Needs a Logo Design & Business Card Design

Design wanted: Logo and Business Card Design for an online store selling designer gifts (substantially Scandinavian design products). Business Card to feature Logo and company details on the front and the back to include discount/promotional code.

Site name: Gift Picks in Minutes

Site purpose: Enable time poor people to quickly select high design value gifts for special occasions (weddings, anniversaries, housewarmings, corporate gifts etc)

Products: A small selection of carefully selected high design value products ranging in price and across three categories: Display, Functional, Fun

Site design: We will be using a modern minimal Shopify theme and will also have a mobile site and an app. Our website is primarily black/white/grayscale - similar to this style: http://templates.vendorapla.com/templates/clean/styles/apparel

Target Market(s)

Customers with limited time who can quickly choose a gift from our pre selected range of 24 products.

Industry/Entity Type

Store

Logo Text

Gift Picks In Minutes

Requirements
Must have
• Modern design with company name included in the design, design needs to be modern and work well with our website - sample website (http://templates.vendorapla.com/templates/clean/styles/apparel).

```html
<!DOCTYPE html>
<html lang="en">
<head>
<meta charset="utf-8">
<title>Gift Picks in Minutes — Business Card</title>
<link rel="stylesheet" href="https://fonts.googleapis.com/css2?family=Cutive&display=swap">
<style>
  :root {
    --canvas: #dcdcdc;
    --card: #ffffff;
    --shadow-soft: #b9b9b9;
    --shadow-deep: #8a8a8a;
    --badge: #2b2b2b;
    --badge-text: #f2f2f2;
    --body-text: #555555;
    --pattern-dark: #2e2e2e;
    --pattern-light: #8c8c8c;
  }
  * { margin: 0; padding: 0; box-sizing: border-box; }
  html, body { width: 1200px; height: 1000px; overflow: hidden; }
  body {
    position: relative;
    background: var(--canvas);
    font-family: "Cutive", "Courier New", serif;
  }
  .card-shadow { position: absolute; }
  .card-shadow--front { left: 249px; top: 80px; width: 700px; height: 388px; background: var(--shadow-soft); }
  .card-shadow--back { left: 256px; top: 550px; width: 695px; height: 388px; background: var(--shadow-deep); }
  .card {
    position: absolute;
    background: var(--card);
    overflow: hidden;
  }
  .card--front { left: 243px; top: 74px; width: 700px; height: 388px; }
  .card--back { left: 243px; top: 538px; width: 698px; height: 388px; }
  .card__pattern {
    position: absolute; left: 0; top: 0; width: 350px; height: 100%;
    background: linear-gradient(135deg, var(--pattern-dark), var(--pattern-light));
  }
  .badge {
    position: absolute;
    width: 236px; height: 236px; border-radius: 50%;
    background: var(--badge);
    color: var(--badge-text);
    text-align: center;
  }
  .card--front .badge { left: 53px; top: 78px; }
  .card--back .badge { left: 50px; top: 83px; }
  .badge__name {
    position: absolute; left: 0; right: 0; top: 74px;
    font-size: 22px; line-height: 31px; letter-spacing: 1px;
    text-transform: uppercase;
  }
  .badge__amount {
    position: absolute; left: 0; right: 0; top: 46px;
    font-size: 80px; line-height: 90px;
  }
  .badge__currency {
    font-size: 32px; vertical-align: 30px; margin-right: 8px;
  }
  .badge__caption {
    position: absolute; left: 0; right: 0; top: 139px;
    font-size: 19px; line-height: 24px;
  }
  .card__info {
    position: absolute; left: 408px;
    color: var(--body-text);
  }
  .card--front .card__info { top: 115px; font-size: 18px; line-height: 22px; }
  .card__info p + p { margin-top: 13px; }
  .card--back .card__info { top: 140px; }
  .promo__label, .promo__code { font-size: 21px; line-height: 29px; }
  .promo__terms { margin-top: 17px; font-size: 14.5px; line-height: 21px; width: 220px; }
</style>
</head>
<body>
  <div class="card-shadow card-shadow--front"></div>
  <section class="card card--front">
    <div class="card__pattern" role="img" aria-label="Black and white herringbone chevron pattern"></div>
    <div class="badge">
      <div class="badge__name">Gift Picks<br>In<br>Minutes</div>
    </div>
    <div class="card__info">
      <p>//high design value gifts<br>for special occasions</p>
      <p>//carefully selected high<br>design value products</p>
      <p>//three categories:<br>display, function, fun.</p>
    </div>
  </section>

  <div class="card-shadow card-shadow--back"></div>
  <section class="card card--back">
    <div class="card__pattern" role="img" aria-label="Black and white herringbone chevron pattern"></div>
    <div class="badge">
      <div class="badge__amount"><span class="badge__currency">$</span>20</div>
      <div class="badge__caption">special gift to you*</div>
    </div>
    <div class="card__info">
      <p class="promo__label">//enter code:</p>
      <p class="promo__code">3AW1415jjbF</p>
      <p class="promo__terms">*minimum spend $79 on full priced items only. valid until 17/7/14.</p>
    </div>
  </section>
</body>
</html>
```